Business Card Design using new logo

As much as we'd like to think that treating everyone equally is the best strategy for fairness, the reality is that the differences in the lives of women and men have to be taken into account to ensure that organizations, programs, services, and yes, even public policy treat women and men in ways that achieve gender equity.

That's where ParityLumen - fairness metrics insight comes in. Using the data-driven tools of gender analysis, our organization can help anyone determine if gender equity is being achieved - in businesses and organizations, in the planning and implementation of programs and services, and in the development and enforcement of public policy.
Updates

Apologies for the delay - have not had time to finalize the decision.  Should be early this week - probably Tuesday.

Industry/Entity Type

Business

Requirements
Must have
• New Logo for ParityLumen
• Logo plus words "Fairness Metrics Insight"

```html
<!DOCTYPE html>
<html lang="en">
<head>
<meta charset="utf-8">
<title>ParityLumen Business Cards</title>
<link href="https://fonts.googleapis.com/css2?family=Saira:wght@500;700&family=Michroma&display=swap" rel="stylesheet">
<style>
  :root {
    --page-bg: #d9d9d9;
    --card-dark: #1c1c1c;
    --card-grey: #8c8c8c;
    --band-orange: #d9521a;
    --band-amber: #e89a10;
    --band-charcoal: #2e2e2e;
    --text-light: #eeeeee;
    --text-dark: #111111;
    --accent-orange: #e8870f;
    --frame-line: #3a3a3a;
  }
  * { margin: 0; padding: 0; box-sizing: border-box; }
  html, body { width: 1200px; height: 1000px; overflow: hidden; }
  body {
    background: var(--page-bg);
    font-family: "Michroma", sans-serif;
    position: relative;
  }
  .card {
    position: absolute;
    left: 250px;
    width: 700px;
    height: 400px;
    overflow: hidden;
    box-shadow: 0 6px 18px rgba(0,0,0,0.25);
  }

  /* Front card */
  .card--front { top: 60px; background: var(--card-grey); }
  .card__frame {
    position: absolute;
    inset: 22px;
    border: 3px double var(--frame-line);
  }
  .brand {
    position: absolute;
    display: flex;
    align-items: center;
    gap: 16px;
    font-family: "Saira", sans-serif;
    font-weight: 700;
  }
  .brand__mark {
    width: 64px; height: 64px;
    border-radius: 50%;
    background: var(--accent-orange);
  }
  .card--front .brand { left: 110px; top: 140px; }
  .card--front .brand__name { font-size: 70px; line-height: 1; color: var(--text-dark); }
  .tagline {
    position: absolute;
    left: 190px; top: 225px;
    font-family: "Saira", sans-serif;
    font-weight: 700;
    font-size: 24px;
    letter-spacing: 2px;
    color: #ffffff;
  }

  /* Back card */
  .card--back { top: 540px; background: var(--card-dark); }
  .card--back .brand { left: 200px; top: 44px; }
  .card--back .brand__mark { width: 52px; height: 52px; }
  .card--back .brand__name { font-size: 54px; line-height: 1; color: var(--text-light); font-weight: 500; }
  .band {
    position: absolute; left: 0; width: 100%;
    display: flex; align-items: center; justify-content: center; gap: 90px;
    color: var(--text-light);
    font-size: 15px;
    letter-spacing: 2px;
  }
  .band--orange { top: 160px; height: 44px; background: var(--band-orange); }
  .band--amber { top: 212px; height: 44px; background: var(--band-amber); color: var(--text-dark); }
  .band--charcoal { top: 264px; height: 50px; background: var(--band-charcoal); font-size: 13px; }
  .contact { display: flex; align-items: center; gap: 8px; }
  .contact svg { width: 16px; height: 16px; flex: none; }
  .social {
    position: absolute; top: 335px; left: 0; width: 100%;
    display: flex; justify-content: center; align-items: center; gap: 8px;
    color: var(--text-light); font-size: 12px; letter-spacing: 1px;
  }
  .social__dot { width: 12px; height: 12px; border-radius: 50%; background: #3a8fd6; }
</style>
</head>
<body>

<section class="card card--front">
  <div class="card__frame"></div>
  <div class="brand">
    <span class="brand__mark"></span>
    <span class="brand__name">ParityLumen</span>
  </div>
  <div class="tagline">Fairness Metrics Insight</div>
</section>

<section class="card card--back">
  <div class="brand">
    <span class="brand__mark"></span>
    <span class="brand__name">ParityLumen</span>
  </div>
  <div class="band band--orange">Name LastName</div>
  <div class="band band--amber">
    <span class="contact">
      <svg viewBox="0 0 16 16"><path d="M4 1h3l1 4-2 1.5a9 9 0 0 0 3.5 3.5L11 8l4 1v3c0 1-1 2-2 2A12 12 0 0 1 2 3c0-1 1-2 2-2z" fill="#1a1a1a"/></svg>
      123456789
    </span>
    <span class="contact">
      <svg viewBox="0 0 16 16"><rect x="4" y="1" width="8" height="14" rx="1.5" fill="#1a1a1a"/><rect x="5.5" y="3" width="5" height="8" fill="#e89a10"/></svg>
      123456789
    </span>
  </div>
  <div class="band band--charcoal">
    <span class="contact">
      <svg viewBox="0 0 16 16"><circle cx="8" cy="8" r="6.5" fill="none" stroke="#e8870f" stroke-width="1.5"/><path d="M1.5 8h13M8 1.5c-3 3.5-3 9.5 0 13M8 1.5c3 3.5 3 9.5 0 13" fill="none" stroke="#e8870f" stroke-width="1.2"/></svg>
      paritylumen.com
    </span>
    <span class="contact">
      <svg viewBox="0 0 16 16"><rect x="1" y="3" width="14" height="10" rx="1" fill="none" stroke="#e8870f" stroke-width="1.5"/><path d="M1.5 3.5 8 9l6.5-5.5" fill="none" stroke="#e8870f" stroke-width="1.5"/></svg>
      Email@paritylumen.com
    </span>
  </div>
  <div class="social">
    <span class="social__dot"></span>
    @Parity_Lumen
  </div>
</section>

</body>
</html>
```